LEARN Business Skills so you can Earn a good living

size of the poster is 8”x 10.75" plus 0.25" bleed.
Please leave 1 inch on the bottoum for footer
I want a design a poster that will attract people's attention.
I appreciate a creative ad however the ad should not take away from being able to clearly read the text.
-I also appreciate a simple creative ad that is not too busy.
-you can use graphics, vectors, or pictures of real people.
-however, if you use real people it should be a white male that is wearing a white shirt and look like a professional person.

Target Market(s)

Potential young business people

Industry/Entity Type

education

Requirements
Must have
• easy to read the text
Nice to have
• I would like a "creative" simple ad that is easy to be read
Should not have
• pictures of women

```html
<!DOCTYPE html>
<html lang="en">
<head>
<meta charset="UTF-8">
<title>Business Enrichment Course Poster</title>
<link href="https://fonts.googleapis.com/css2?family=DM+Sans:ital,wght@0,400;0,500;0,700;1,500&family=Playfair+Display:wght@900&display=swap" rel="stylesheet">
<style>
  :root {
    --stage: #e6e7e9;
    --paper: #eeeff1;
    --navy: #2a3f7a;
    --navy-deep: #1f2f5e;
    --blue: #2f5bab;
    --orange: #ec8a2b;
    --ink: #26325a;
    --rule: #c9cbd0;
    --sky-light: #e9eaec;
    --sky-mid: #d9dadd;
  }
  * { margin: 0; padding: 0; box-sizing: border-box; }
  html, body { width: 1200px; height: 1200px; overflow: hidden; background: var(--stage); }
  .poster {
    position: absolute; left: 188px; top: 20px;
    width: 824px; height: 1160px;
    background: var(--paper);
    overflow: hidden;
    font-family: "DM Sans", sans-serif;
    color: var(--ink);
  }
  .skyline {
    position: absolute; left: 0; top: 0; width: 824px; height: 680px;
    background: linear-gradient(180deg, var(--sky-light) 0%, var(--sky-mid) 55%, var(--paper) 100%);
    opacity: 0.8;
  }
  .brand {
    position: absolute; left: 62px; top: 78px;
    font-family: "DM Sans", sans-serif; font-weight: 700;
    font-size: 60px; line-height: 0.98; letter-spacing: -1px;
    color: var(--navy);
  }
  .hero-art {
    position: absolute; left: 37px; top: 328px; width: 240px; height: 224px;
    background: linear-gradient(135deg, #dfe3ec 0%, #9fb3dc 55%, var(--blue) 100%);
    border-radius: 6px;
  }
  .title {
    position: absolute; left: 289px; top: 330px;
    font-family: "Playfair Display", serif; font-weight: 900;
    font-size: 72px; line-height: 71px; color: var(--navy);
    letter-spacing: -0.5px;
  }
  .tagline {
    position: absolute; left: 0; width: 100%; top: 592px; text-align: center;
    font-style: italic; font-weight: 500; font-size: 26.5px; color: var(--orange);
  }
  .benefits { position: absolute; left: 0; top: 670px; width: 100%; height: 200px; }
  .benefit { position: absolute; top: 2px; width: 240px; text-align: center; }
  .benefit-tile {
    width: 116px; height: 114px; margin: 0 auto;
    border-radius: 26px 26px 0 26px;
    background: linear-gradient(135deg, var(--navy-deep), var(--blue));
  }
  .benefit-label { margin-top: 11px; font-size: 25px; line-height: 28px; font-weight: 500; color: var(--ink); }
  .divider { position: absolute; top: 0; width: 1px; height: 190px; background: var(--rule); }
  .topics {
    position: absolute; left: 30px; right: 30px; top: 902px;
    text-align: center; font-size: 17.8px; line-height: 29.4px; color: var(--ink);
  }
  .topics .sep { color: var(--orange); padding: 0 3px; }
</style>
</head>
<body>
<main class="poster">
  <div class="skyline" role="img" aria-label="Faded photograph of a city skyline with a tall spired skyscraper"></div>

  <div class="brand">SKILL<br>LADDER</div>

  <div class="hero-art" role="img" aria-label="Illustration of a businessman with a laptop leaning on a rising blue arrow, briefcase beside him"></div>

  <h1 class="title">BUSINESS<br>ENRICHMENT<br>COURSE</h1>

  <p class="tagline">A proven success of helping people in their livelihoods</p>

  <section class="benefits">
    <div class="benefit" style="left:10px">
      <div class="benefit-tile" role="img" aria-label="Icon illustration for finding a quality job"></div>
      <p class="benefit-label">Get a<br>Quality Job</p>
    </div>
    <div class="divider" style="left:255px"></div>
    <div class="benefit" style="left:273px">
      <div class="benefit-tile" role="img" aria-label="Icon illustration for starting and growing a business"></div>
      <p class="benefit-label">Start/Grow<br>Your Business</p>
    </div>
    <div class="divider" style="left:532px"></div>
    <div class="benefit" style="left:549px">
      <div class="benefit-tile" role="img" aria-label="Icon illustration for increasing salary"></div>
      <p class="benefit-label">Increase Your<br>Salary</p>
    </div>
  </section>

  <p class="topics">
    Business Administration<span class="sep">|</span>Small Business Management<span class="sep">|</span>Finance<span class="sep">|</span>Investments<span class="sep">|</span><br>
    Computers<span class="sep">|</span>Accounting<span class="sep">|</span>Sales Marketing<span class="sep">|</span>Project Management Interviewing Skills<span class="sep">|</span><br>
    Business Law<span class="sep">|</span>Negotiation<span class="sep">|</span>Public Speaking<span class="sep">|</span>Import/Export<span class="sep">|</span>Information Technoloy<span class="sep">|</span><br>
    Distribution<span class="sep">|</span>Marketing<span class="sep">|</span>Ledgerly<span class="sep">|</span>Real Estate<span class="sep">|</span>Health Care<span class="sep">|</span>Management<span class="sep">|</span>Rivermart
  </p>
</main>
</body>
</html>
```